Electrician Business needs flyer for discount offer and advertise services

Need a promotional flyer that will grab attention,, offer:

During the months of October & November receive a 10% discount on;
Ceiling fan installation
Smoke alarm installation
Replace existing downlights for new LED downlights.
Offer expires 30th November 2016
'Keep cool, stay safe and save power with VoltMate'

Would like to advertise services and quality on reverse-side. Can have graphic pointing to reverse side on both sides, encouraging customer to read both sides of flyer.
Contact details both sides
Design to suit two-sided A5

Reverse side list services;

All residential & commercial electrical services
Electrical contracting
Real estate/strata electrical maintenance & repairs
New builds
Renovations
Security sensor lighting
Ceiling fans
Smoke Alarms
Data connections

Target Market(s)

Residential home owners and commercial, building and construction companies

Industry/Entity Type

Electrical

Font styles to use
Serif

Colors
0255a3
ffffff

Requirements
Nice to have
• A picture of a modern ceiling fan.
• Arrow/graphic pointing to reverse side, so customer reads both sides of flyer

```html
<!DOCTYPE html>
<html lang="en">
<head>
<meta charset="utf-8">
<title>VoltMate Electrical Services – October &amp; November Offer</title>
<link rel="stylesheet" href="https://fonts.googleapis.com/css2?family=Cinzel:wght@700&family=Oswald:wght@500;700&family=Roboto+Condensed:wght@400&display=swap">
<style>
  :root {
    --white: #ffffff;
    --orange: #f26522;
    --deep: #2f3a82;
    --mid: #5b66ad;
    --glow: #c3c7e8;
    --footer: #27347a;
    --panel: rgba(255,255,255,0.16);
    --icon-ink: #2f3a82;
  }
  * { margin: 0; padding: 0; box-sizing: border-box; }
  html, body { width: 856px; height: 1200px; overflow: hidden; background: var(--white); }
  .flyer {
    position: relative; width: 856px; height: 1200px; overflow: hidden;
    background: radial-gradient(ellipse 70% 45% at 50% 34%, var(--glow) 0%, var(--mid) 55%, var(--deep) 100%);
    color: var(--white);
    font-family: "Oswald", sans-serif;
  }
  .brand { position: absolute; top: 100px; left: 0; width: 100%; text-align: center; }
  .brand-name {
    font-family: "Oswald", sans-serif; font-weight: 700; font-size: 96px;
    line-height: 1; letter-spacing: 2px; color: var(--white);
  }
  .brand-tag {
    margin-top: 10px; font-family: "Oswald", sans-serif; font-weight: 700;
    font-size: 36px; letter-spacing: 1px; color: var(--white);
  }
  .offer-lead {
    position: absolute; left: 0; width: 100%; text-align: center;
    font-family: "Cinzel", serif; font-weight: 700; color: var(--white);
    text-shadow: 0 2px 3px rgba(0,0,0,0.35);
  }
  .offer-lead.line-one { top: 312px; font-size: 30px; }
  .offer-lead.line-two { top: 366px; font-size: 25px; display: flex; justify-content: center; align-items: center; gap: 14px; }
  .offer-lead .big { font-size: 31px; }
  .chevrons { width: 72px; height: 30px; }
  .photo-band {
    position: absolute; top: 690px; left: 0; width: 100%; height: 244px;
    background: rgba(255,255,255,0.12);
  }
  .service {
    position: absolute; top: 451px; width: 232px; height: 252px;
    background: var(--panel); border-top: 13px solid var(--orange);
    display: flex; flex-direction: column; align-items: center; justify-content: center;
    text-transform: uppercase; font-weight: 500; line-height: 0.98; text-align: center;
    text-shadow: 0 2px 3px rgba(0,0,0,0.3);
  }
  .service.fan { left: 39px; }
  .service.alarm { left: 309px; }
  .service.downlight { left: 582px; }
  .service .s { font-size: 34px; }
  .service .m { font-size: 66px; }
  .service .l { font-size: 96px; }
  .service .xs { font-size: 30px; }
  .service-photo {
    position: absolute; top: 723px; width: 232px; height: 176px;
    border: 1px solid rgba(255,255,255,0.7);
  }
  .service-photo.fan { left: 39px; background: linear-gradient(160deg, #9a9ba3, #5e6068 60%, #3b3c42); }
  .service-photo.alarm { left: 309px; background: radial-gradient(circle at 55% 45%, #e4e4e4, #a9aaa9 70%, #8c8d8c); }
  .service-photo.downlight { left: 582px; background: radial-gradient(circle at 50% 40%, #8a867c, #3b3934 60%, #1d1c1a); }
  .tagline {
    position: absolute; top: 934px; left: 0; width: 100%; height: 82px;
    display: flex; align-items: center; justify-content: center;
    font-family: "Roboto Condensed", sans-serif; font-size: 33px;
    background: rgba(40,52,120,0.35);
    border-bottom: 2px solid rgba(255,255,255,0.7);
  }
  .contact-bar {
    position: absolute; top: 1016px; left: 0; width: 100%; height: 184px;
    background: linear-gradient(180deg, #34418c, var(--footer));
  }
  .contact-list { position: absolute; top: 20px; left: 30px; list-style: none; }
  .contact-list li {
    display: flex; align-items: center; gap: 16px; height: 40px;
    font-family: "Roboto Condensed", sans-serif; font-size: 24px;
  }
  .contact-list svg { width: 30px; height: 30px; flex: none; }
  .expiry {
    position: absolute; right: 28px; top: 118px; text-align: right;
    font-family: "Cinzel", serif; font-weight: 700; line-height: 1.25;
  }
  .expiry .small { font-size: 21px; }
  .expiry .date { font-size: 25px; }
</style>
</head>
<body>
<main class="flyer">
  <header class="brand">
    <div class="brand-name">VoltMate</div>
    <div class="brand-tag">Electrical Services</div>
  </header>

  <p class="offer-lead line-one">During the months of October &amp; November</p>
  <p class="offer-lead line-two">
    <svg class="chevrons" viewBox="0 0 72 30" aria-hidden="true">
      <g fill="var(--orange)"><polygon points="0,0 14,0 28,15 14,30 0,30 14,15"/><polygon points="22,0 36,0 50,15 36,30 22,30 36,15"/><polygon points="44,0 58,0 72,15 58,30 44,30 58,15"/></g>
    </svg>
    <span>Receive a <span class="big">10%</span> discount on</span>
    <svg class="chevrons" viewBox="0 0 72 30" aria-hidden="true">
      <g fill="var(--orange)"><polygon points="72,0 58,0 44,15 58,30 72,30 58,15"/><polygon points="50,0 36,0 22,15 36,30 50,30 36,15"/><polygon points="28,0 14,0 0,15 14,30 28,30 14,15"/></g>
    </svg>
  </p>

  <div class="photo-band"></div>

  <section class="service fan"><span class="m">Ceiling</span><span class="l">Fan</span><span class="s">Installation</span></section>
  <section class="service alarm"><span class="m" style="font-size:74px">Smoke</span><span class="m" style="font-size:74px">Alarm</span><span class="s" style="font-size:38px">Installation</span></section>
  <section class="service downlight"><span class="xs">Replace existing</span><span class="xs">downlights for</span><span class="m" style="font-size:70px">New LED</span><span class="s" style="font-size:44px">Downlights</span></section>

  <div class="service-photo fan" role="img" aria-label="Photo of a ceiling fan with a lit centre light"></div>
  <div class="service-photo alarm" role="img" aria-label="Photo of a ceiling-mounted smoke alarm"></div>
  <div class="service-photo downlight" role="img" aria-label="Photo of several round LED downlights"></div>

  <p class="tagline">'Keep cool, stay safe and save power with VoltMate'</p>

  <footer class="contact-bar">
    <ul class="contact-list">
      <li>
        <svg viewBox="0 0 30 30" aria-hidden="true"><circle cx="15" cy="15" r="15" fill="var(--white)"/><path d="M10 7 l4 4 -2 2 c1 2 3 4 5 5 l2 -2 4 4 -2 3 c-6 0 -13 -7 -13 -13z" fill="var(--icon-ink)"/></svg>
        0198765432
      </li>
      <li>
        <svg viewBox="0 0 30 30" aria-hidden="true"><circle cx="15" cy="15" r="15" fill="var(--white)"/><g fill="none" stroke="var(--icon-ink)" stroke-width="1.6"><circle cx="15" cy="15" r="9"/><ellipse cx="15" cy="15" rx="4" ry="9"/><line x1="6" y1="15" x2="24" y2="15"/><line x1="8" y1="10" x2="22" y2="10"/><line x1="8" y1="20" x2="22" y2="20"/></g></svg>
        www.voltmate.com
      </li>
      <li>
        <svg viewBox="0 0 30 30" aria-hidden="true"><circle cx="15" cy="15" r="15" fill="var(--white)"/><rect x="7" y="10" width="16" height="11" fill="var(--icon-ink)"/><path d="M7 10 l8 6 8 -6" fill="none" stroke="var(--white)" stroke-width="1.4"/></svg>
        info@voltmate.com
      </li>
      <li>
        <svg viewBox="0 0 30 30" aria-hidden="true"><circle cx="15" cy="15" r="15" fill="var(--white)"/><path d="M15 6 a6 6 0 0 1 6 6 c0 5 -6 12 -6 12 s-6 -7 -6 -12 a6 6 0 0 1 6 -6z" fill="var(--icon-ink)"/><circle cx="15" cy="12" r="2.3" fill="var(--white)"/></svg>
        48 Ampere Lane, Riverton CITY 054321
      </li>
    </ul>
    <div class="expiry">
      <div class="small">Offer expires</div>
      <div class="date">30th November 2016</div>
    </div>
  </footer>
</main>
</body>
</html>
```